Business Card, Stationary with Shark Logo for Personal Injury Lawyer

I need business cards and stationery with a shark logo for my Personal Injury Law Practice. Has to have this written on it:
Martin K. Hollis
Injury Lawyer
The Corvell Building
718 Tandy Street
Providence, Rhode Island 02908
401-627-4193
Martinhollis.com

Contact Information for Business Card

Martin K. Hollis, Injury Lawyer, address, 401-627-4193, martinhollis.com

```html
<!DOCTYPE html>
<html lang="en">
<head>
<meta charset="utf-8">
<title>Martin K. Hollis – Business Card</title>
<link rel="stylesheet" href="https://fonts.googleapis.com/css2?family=Montserrat:wght@500;600;800&family=Roboto:wght@400&display=swap">
<style>
  :root {
    --backdrop: #1c1c20;
    --card-white: #ffffff;
    --card-tint: #f1f1f4;
    --brand-purple: #3d3190;
    --brand-purple-deep: #2a2070;
    --brand-purple-light: #4a3ba8;
    --text-grey: #5a5a60;
    --logo-white: #f4f4f8;
  }
  * { box-sizing: border-box; margin: 0; padding: 0; }
  html, body {
    width: 1200px; height: 900px; overflow: hidden;
    background: var(--backdrop);
  }
  .canvas {
    width: 1200px; height: 900px;
    display: flex; flex-direction: column;
    align-items: center; justify-content: center; gap: 60px;
  }
  .card {
    width: 630px; height: 360px;
    position: relative;
    border-radius: 4px;
    box-shadow: 0 14px 30px rgba(0,0,0,.5);
    overflow: hidden;
  }

  /* Front */
  .card--front {
    background: linear-gradient(100deg, var(--card-tint) 0%, var(--card-white) 45%);
  }
  .holder {
    position: absolute; left: 40px; top: 160px;
    font-family: "Montserrat", sans-serif;
  }
  .holder__name {
    color: var(--brand-purple);
    font-weight: 600; font-size: 19px; letter-spacing: .5px;
    text-transform: uppercase;
    white-space: nowrap;
  }
  .holder__title {
    color: var(--text-grey);
    font-weight: 500; font-size: 17px; margin-top: 2px;
  }
  .wordmark {
    font-family: "Montserrat", sans-serif;
    font-weight: 800; text-transform: uppercase;
    text-align: center; line-height: 1.05;
    white-space: nowrap;
  }
  .card--front .wordmark {
    position: absolute; right: 34px; top: 66px; width: 290px;
    color: var(--brand-purple);
    font-size: 27px;
  }
  .wordmark__sub { display: block; font-size: .5em; letter-spacing: 4px; margin-top: 6px; }
  .contact {
    position: absolute; left: 318px; top: 178px;
    font-family: "Roboto", sans-serif;
    font-size: 17px; color: var(--text-grey);
    list-style: none; line-height: 1.45;
    white-space: nowrap;
  }
  .contact__line { display: flex; align-items: center; gap: 8px; }
  .contact__line--plain { padding-left: 24px; }
  .contact__icon { width: 16px; height: 16px; flex: none; }

  /* Back */
  .card--back {
    background: linear-gradient(135deg, var(--brand-purple-light) 0%, var(--brand-purple) 45%, var(--brand-purple-deep) 100%);
    display: flex; align-items: center; justify-content: center;
  }
  .card--back .wordmark {
    color: var(--logo-white);
    font-size: 52px;
  }
</style>
</head>
<body>
<main class="canvas">

  <section class="card card--front" aria-label="Business card front">
    <div class="holder">
      <p class="holder__name">Martin K. Hollis</p>
      <p class="holder__title">Injury Lawyer</p>
    </div>

    <p class="wordmark">Martin K. Hollis<span class="wordmark__sub">Injury Lawyer</span></p>

    <ul class="contact">
      <li class="contact__line contact__line--plain">718 Tandy St</li>
      <li class="contact__line contact__line--plain">Larkport, RI 02914</li>
      <li class="contact__line">
        <svg class="contact__icon" viewBox="0 0 16 16" aria-hidden="true"><path fill="#3d3190" d="M4 1.5l2.2 3-1.3 1.6c.8 1.8 2.2 3.3 4 4.1l1.6-1.3 3 2.2-1.3 2.6C7.5 13.5 2.5 8.5 1.6 2.8z"/></svg>
        (401) 627-4193
      </li>
      <li class="contact__line">
        <svg class="contact__icon" viewBox="0 0 16 16" aria-hidden="true"><rect x="1" y="3" width="14" height="10" fill="#3d3190"/><path d="M1.5 3.5L8 9l6.5-5.5" fill="none" stroke="#fff" stroke-width="1.2"/></svg>
        martin@martinhollis.com
      </li>
      <li class="contact__line">
        <svg class="contact__icon" viewBox="0 0 16 16" aria-hidden="true"><circle cx="8" cy="8" r="6.5" fill="none" stroke="#3d3190" stroke-width="1.4"/><path d="M1.5 8h13M8 1.5c-2.5 3-2.5 10 0 13M8 1.5c2.5 3 2.5 10 0 13" fill="none" stroke="#3d3190" stroke-width="1.1"/></svg>
        www.martinhollis.com
      </li>
    </ul>
  </section>

  <section class="card card--back" aria-label="Business card back">
    <p class="wordmark">Martin K. Hollis<span class="wordmark__sub">Injury Lawyer</span></p>
  </section>

</main>
</body>
</html>
```